Velora Aesthetica

Medical doctor providing aesthetic medicine

* Double sided card
* Logo to be on card
Other details:
* Dr. Mirela Kostvan, BSc, MBChB, CCFP
* #214-215, 27903 83 Ave, Surrey, BC, V2T 4K7
* 604-718-2943
* info@veloraclinic.ca
* www.veloraclinic.ca

Industry/Entity Type

Medical / Health & Beauty

Contact Information for Business Card

see 'Project Description'

Colors
0054AA
0677BA
7BADD7
CADEEF
E8F1F8
FFF300
FFF600
FEFA6F
FFFEC7
FFFEE8

Requirements
Must have
• Modern, high-end design

```html
<!DOCTYPE html>
<html lang="en">
<head>
<meta charset="utf-8">
<title>Velora Aesthetica — Business Card</title>
<link rel="stylesheet" href="https://fonts.googleapis.com/css2?family=Montserrat:wght@400;500&family=Inter:wght@700&family=Source+Sans+3:wght@600&display=swap">
<style>
  :root {
    --stage: #000000;
    --navy: #214263;
    --ink: #1f4466;
    --gold: #c9a42c;
    --paper: #ffffff;
    --rule: #1a1a1a;
  }
  * { margin: 0; padding: 0; box-sizing: border-box; }
  html, body { width: 1200px; height: 1200px; overflow: hidden; background: var(--stage); }
  .stage { position: relative; width: 1200px; height: 1200px; }

  .card {
    position: absolute;
    left: 334px;
    width: 531px;
    height: 318px;
    border-radius: 38px;
    overflow: hidden;
  }
  .card--front { top: 300px; background: var(--navy); }
  .card--back { top: 637px; background: var(--paper); }

  .card__texture { position: absolute; inset: 0; background: var(--navy); }

  .wordmark {
    position: absolute;
    left: 0; right: 0;
    text-align: center;
    font-family: "Montserrat", sans-serif;
    font-weight: 500;
    color: var(--gold);
    text-transform: uppercase;
    letter-spacing: 0.32em;
    line-height: 1.15;
  }
  .card--front .wordmark { top: 128px; font-size: 28px; }
  .card--back .wordmark { top: 46px; font-size: 24px; }
  .wordmark span { display: block; padding-left: 0.32em; }

  .person { position: absolute; left: 34px; top: 193px; color: var(--ink); }
  .person__name { font-family: "Inter", sans-serif; font-weight: 700; font-size: 25px; letter-spacing: -0.02em; line-height: 1.1; }
  .person__creds { font-family: "Montserrat", sans-serif; font-weight: 400; font-size: 13.5px; margin-top: 2px; }

  .divider { position: absolute; left: 277px; top: 165px; width: 2px; height: 109px; background: var(--rule); }

  .contacts {
    position: absolute; left: 321px; top: 166px;
    list-style: none;
    font-family: "Source Sans 3", sans-serif; font-weight: 600; font-size: 13.5px;
    color: var(--ink); line-height: 1.2;
  }
  .contacts li { display: flex; align-items: flex-start; gap: 5px; margin-bottom: 4.5px; }
  .contacts svg { width: 11px; height: 11px; flex: none; margin-top: 3px; fill: var(--ink); }
</style>
</head>
<body>
<main class="stage">
  <section class="card card--front">
    <div class="card__texture" role="img" aria-label="Subtle repeating tonal pattern on navy"></div>
    <div class="wordmark"><span>Velora</span><span>Aesthetica</span></div>
  </section>

  <section class="card card--back">
    <div class="wordmark"><span>Velora</span><span>Aesthetica</span></div>

    <div class="person">
      <h1 class="person__name">Dr. Mirela Kostvan</h1>
      <p class="person__creds">BSc, MBChB, CCFP</p>
    </div>

    <div class="divider"></div>

    <ul class="contacts">
      <li>
        <svg viewBox="0 0 24 24"><path d="M6.6 10.8a15.1 15.1 0 0 0 6.6 6.6l2.2-2.2c.3-.3.7-.4 1-.2 1.1.4 2.3.6 3.6.6.6 0 1 .4 1 1V20c0 .6-.4 1-1 1A17 17 0 0 1 3 4c0-.6.4-1 1-1h3.5c.6 0 1 .4 1 1 0 1.3.2 2.5.6 3.6.1.3 0 .7-.2 1z"/></svg>
        <span>604-718-2943</span>
      </li>
      <li>
        <svg viewBox="0 0 24 24"><path d="M2 5h20v14H2zm2 2v.4l8 5.3 8-5.3V7zm16 2.8-8 5.3-8-5.3V17h16z"/></svg>
        <span>info@veloraclinic.ca</span>
      </li>
      <li>
        <svg viewBox="0 0 24 24"><path d="M12 2a10 10 0 1 0 0 20 10 10 0 0 0 0-20zm7.9 9h-3.4a15 15 0 0 0-1.4-6.3A8 8 0 0 1 19.9 11zM12 4.1c1 1.3 2.3 3.7 2.5 6.9h-5C9.7 7.8 11 5.4 12 4.1zM8.9 4.7A15 15 0 0 0 7.5 11H4.1a8 8 0 0 1 4.8-6.3zM4.1 13h3.4a15 15 0 0 0 1.4 6.3A8 8 0 0 1 4.1 13zm7.9 6.9c-1-1.3-2.3-3.7-2.5-6.9h5c-.2 3.2-1.5 5.6-2.5 6.9zm3.1-.6a15 15 0 0 0 1.4-6.3h3.4a8 8 0 0 1-4.8 6.3z"/></svg>
        <span>www.veloraclinic.ca</span>
      </li>
      <li>
        <svg viewBox="0 0 24 24"><path d="M12 2a7 7 0 0 0-7 7c0 5.2 7 13 7 13s7-7.8 7-13a7 7 0 0 0-7-7zm0 9.5a2.5 2.5 0 1 1 0-5 2.5 2.5 0 0 1 0 5z"/></svg>
        <span>#214-215, 27903 83 Ave,<br>Surrey, BC, V2T 4K7</span>
      </li>
    </ul>
  </section>
</main>
</body>
</html>
```